Brenmore Land Clearing postcard ( for direct mailing) and business card design

Design postcards/Business cards
Dale Hartwick
Brenmore Land Clearing
462 Quillstone Rd Lewisville,NC 27458
(336) 571-2846 Dale@Brenmorelandclearing.example

The postcard will be used for direct mailing to land owners and contractors to advertise our service. Pictures of the process and equipment along with a short summary of what we do. Business card should be contact info and logo.
Updates

The post cards could say something like this: Forestry Mulching machines are capable of clearing land of unwanted trees and brush with limited disturbance to soils or desirable vegetation. Traditional land clearing methods often present an increased risk of erosion by pushing over trees, uprooting the stump and roots, and substantially disturbing soils.In contrast, mulching the vegetation leaves the soil structure intact. The mulched material can be left on the ground and will act as an erosion barrier while returning nutrients back into the soil through decomposition. Over time, grass will naturally grow through the mulch and can be maintained with mowing.

Target Market(s)

Land owners and contractors who need vegetation cleared

Industry/Entity Type

Forestry Mulching

Requirements
Must have
• picture, brief description of service offered, contact info on postcard. Business card should have contact info and logo.
Nice to have
• I like contour lines as a background but I'd like to see other ideas.

```html
<!DOCTYPE html>
<html lang="en">
<head>
<meta charset="utf-8">
<title>Brenmore Land Clearing – Business Card</title>
<link rel="stylesheet" href="https://fonts.googleapis.com/css2?family=Montserrat:wght@500;600;700;800&display=swap">
<style>
  :root {
    --green: #1c6b34;
    --green-bright: #2f9b45;
    --ink: #151515;
    --text: #2a2a2a;
    --paper: #ffffff;
    --page: #ffffff;
  }
  * { margin: 0; padding: 0; box-sizing: border-box; }
  html, body { width: 1200px; height: 2697px; overflow: hidden; background: var(--page); }
  body { position: relative; font-family: "Montserrat", sans-serif; color: var(--text); }

  .card {
    position: absolute; left: 188px; width: 824px; height: 470px;
    background: var(--paper);
    box-shadow: 0 6px 28px rgba(0,0,0,0.22);
    overflow: hidden;
  }
  .card--front { top: 853px; }
  .card--back  { top: 1373px; }

  .wordmark { position: absolute; display: flex; align-items: center; }
  .wordmark__square { background: var(--green); flex: none; }
  .wordmark__name {
    font-weight: 800; color: var(--ink); text-transform: uppercase;
    line-height: 1.02; letter-spacing: 1px;
  }

  .card--front .wordmark { left: 0; right: 0; top: 120px; justify-content: center; gap: 26px; }
  .card--front .wordmark__square { width: 70px; height: 70px; }
  .card--front .wordmark__name { font-size: 54px; }

  .site { position: absolute; left: 0; right: 0; text-align: center; color: var(--text); }
  .site b { color: var(--green); font-weight: 700; }
  .card--front .site { top: 358px; font-size: 22px; letter-spacing: 2.5px; font-weight: 500; }

  .card--back .wordmark { left: 54px; top: 150px; gap: 16px; }
  .card--back .wordmark__square { width: 40px; height: 40px; }
  .card--back .wordmark__name { font-size: 31px; }

  .divider { position: absolute; left: 390px; top: 108px; width: 2px; height: 208px; background: var(--ink); }

  .contact { position: absolute; left: 412px; top: 142px; }
  .contact__name { font-size: 31px; font-weight: 700; color: var(--green); letter-spacing: 0.5px; margin-bottom: 8px; }
  .contact__row { display: flex; align-items: center; gap: 12px; color: var(--ink); }
  .contact__row svg { width: 18px; height: 18px; flex: none; fill: var(--green); }
  .contact__row--phone { font-size: 26px; font-weight: 600; margin-bottom: 6px; }
  .contact__row--small { font-size: 15.5px; font-weight: 500; margin-bottom: 8px; }

  .card--back .site { top: 348px; font-size: 29px; font-weight: 600; }

  .band { position: absolute; left: 0; bottom: 0; width: 100%; height: 24px; }
</style>
</head>
<body>

<section class="card card--front" aria-label="Business card front">
  <div class="wordmark">
    <span class="wordmark__square"></span>
    <span class="wordmark__name">Brenmore<br>Land<br>Clearing</span>
  </div>
  <p class="site">www.<b>Brenmorelandclearing</b>.example</p>
</section>

<section class="card card--back" aria-label="Business card back">
  <div class="wordmark">
    <span class="wordmark__square"></span>
    <span class="wordmark__name">Brenmore<br>Land<br>Clearing</span>
  </div>

  <div class="divider"></div>

  <div class="contact">
    <p class="contact__name">DALE HARTWICK</p>
    <p class="contact__row contact__row--phone">
      <svg viewBox="0 0 24 24" aria-hidden="true"><path d="M3 9c0-3 4-5 9-5s9 2 9 5v2h-5V9H8v2H3zM6 12h12l2 8H4z"/></svg>
      (336) 571-2846
    </p>
    <p class="contact__row contact__row--small">
      <svg viewBox="0 0 24 24" aria-hidden="true"><path d="M3 6h18v13H3zM3 6l9 7 9-7" stroke="#fff" stroke-width="1.5"/></svg>
      Dale@Brenmorelandclearing.example
    </p>
    <p class="contact__row contact__row--small">
      <svg viewBox="0 0 24 24" aria-hidden="true"><path d="M12 2a7 7 0 0 1 7 7c0 5-7 12-7 12S5 14 5 9a7 7 0 0 1 7-7zm0 4a3 3 0 1 0 0 6 3 3 0 0 0 0-6z"/></svg>
      462 Quillstone Rd Lewisville,NC 27458
    </p>
  </div>

  <p class="site">www.<span style="color:var(--green)">Brenmorelandclearing</span>.example</p>

  <svg class="band" viewBox="0 0 824 24" preserveAspectRatio="none" aria-hidden="true">
    <polygon points="0,0 270,0 288,24 0,24" fill="var(--green)"/>
    <polygon points="266,8 824,8 824,24 280,24" fill="var(--ink)"/>
  </svg>
</section>

</body>
</html>
```